Ordinary Velvet Sparrow inquiring into the Mystery of her Heart needs a Book Cover design

Hello! I need a book cover design (for printed softcover 6” x 9” and eBook) for my new book titled "The Wide Season of a Modest Velvet Sparrow: Notes on Finding Room for Every Part." It's the story of a mom juggling a demanding technology career who embarks upon a self-discovery journey, faces cancer, and learns to expand her life, one vulnerable nibble at a time. With the help of a guide on her spiritual path, she learns to let go of her strong woman do-it-all persona, allowing her soul to fully shine. My purpose in writing the book is to share what I've learned about finding the "moreness" in being human.
*I would like to see book cover designs that communicate a sense of both strength and vulnerability, confidence and humbleness, curiosity and inner discovery—hinting at what's to come. I’ve uploaded a few images that I like because they feel clean and simple, and because they can be interpreted as metaphors of the beauty and power within each of us.
*If your design submission includes a mirror reflection of some sort of a “velvet sparrow” image that people are familiar with, then I would like it to convey a reluctant or questioning velvet sparrow, rather than a bold, fighting-to-save-the-world velvet sparrow.
*I lean toward a clean and calming background, as the book is really an inquiry into the mystery of this heart. It’s an examination of what I might have lost of myself, and ultimately gained, through all my crazy years of juggling. So, it’s a journey of spiritual growth.
Thank you for your interest and sharing your creative talent.

Target Market(s)

(1) Career-oriented parents, especially moms, who are in their 30's and 40's, in the midst of the struggle of trying to juggle it all; (2) life-long strivers, age 55+, who are finally slowing down and looking back to try and make sense of their lives, seeking to understand their buried inner life

Industry/Entity Type

Book Categories: Women & Business; Spiritual Self-help; Strong Women

Font styles to use
Serif

Colors

Designer to choose colors to be used in the design.

Requirements
Must have
• Clean and simple overall feeling
Nice to have
• I am open to including color—if so, perhaps some (not too much) hunter green would be nice (not required, but I’ve used it in a draft website design and rather like it).
Should not have
• Should not feel too "busy"

```html
<!DOCTYPE html>
<html lang="en">
<head>
<meta charset="UTF-8">
<title>The Wide Season of a Modest Velvet Sparrow — Book Cover</title>
<link href="https://fonts.googleapis.com/css2?family=Cinzel:wght@400;700&family=Josefin+Sans:wght@300;400&display=swap" rel="stylesheet">
<style>
  :root {
    --stage: #16231f;
    --paper: #dcdcdc;
    --hunter: #1c2b25;
    --ink: #1e1e1e;
    --blush: #e0868a;
    --white: #ffffff;
    --art-top: #d4d4d4;
    --art-bottom: #d9c8c8;
  }
  * { margin: 0; padding: 0; box-sizing: border-box; }
  html, body {
    width: 1200px;
    height: 1200px;
    overflow: hidden;
    background: var(--stage);
  }
  .stage {
    position: relative;
    width: 1200px;
    height: 1200px;
  }
  .cover {
    position: absolute;
    left: 290px;
    top: 135px;
    width: 620px;
    height: 930px;
    background: var(--paper);
    box-shadow: 0 12px 30px rgba(0,0,0,0.45);
  }
  .title-line {
    position: absolute;
    left: 0;
    width: 100%;
    text-align: center;
    font-family: 'Cinzel', serif;
    font-weight: 400;
    font-size: 38px;
    line-height: 1;
    color: var(--ink);
    letter-spacing: 0.5px;
  }
  .title-line--first { top: 66px; }
  .title-line--second { top: 122px; }
  .title-band {
    position: absolute;
    left: 39px;
    top: 166px;
    width: 542px;
    height: 78px;
    background: var(--hunter);
    display: flex;
    align-items: center;
    justify-content: center;
  }
  .title-band__name {
    font-family: 'Cinzel', serif;
    font-weight: 700;
    font-size: 46px;
    line-height: 1;
    color: var(--white);
    letter-spacing: 0.5px;
    padding-top: 4px;
  }
  .subtitle {
    position: absolute;
    left: 0;
    top: 260px;
    width: 100%;
    text-align: center;
    font-family: 'Josefin Sans', sans-serif;
    font-weight: 300;
    font-size: 19px;
    color: var(--blush);
    letter-spacing: 0.6px;
    text-transform: uppercase;
  }
  .cover-art {
    position: absolute;
    left: 215px;
    top: 376px;
    width: 170px;
    height: 294px;
    border-radius: 10px;
    background: linear-gradient(180deg, var(--art-top) 0%, var(--art-bottom) 100%);
  }
  .author {
    position: absolute;
    left: 0;
    top: 806px;
    width: 100%;
    text-align: center;
    font-family: 'Josefin Sans', sans-serif;
    font-weight: 400;
    font-size: 21px;
    color: var(--ink);
    letter-spacing: 0.5px;
  }
</style>
</head>
<body>
  <main class="stage">
    <section class="cover">
      <h1>
        <span class="title-line title-line--first">The Wide Season</span>
        <span class="title-line title-line--second">of a Modest</span>
        <span class="title-band"><span class="title-band__name">VELVET SPARROW</span></span>
      </h1>
      <p class="subtitle">Notes on Finding Room for Every Part</p>
      <div class="cover-art" role="img" aria-label="Line illustration of a figure with flowers growing from an open head, hands held over a heart"></div>
      <p class="author">AUTHOR</p>
    </section>
  </main>
</body>
</html>
```